Veradine Contracting Folder

Creating a design for the cover of our folders that we pass to our customers

Want to keep the same look as our colors and fonts as attached

```html
<!DOCTYPE html>
<html lang="en">
<head>
<meta charset="utf-8">
<title>Veradine Contracting Folder Cover</title>
<link rel="stylesheet" href="https://fonts.googleapis.com/css2?family=Questrial&display=swap">
<style>
  :root {
    --bg-center: #1c5eff;
    --bg-edge: #4a9bf9;
    --brand-blue: #0b2df5;
    --brand-yellow: #fbd723;
    --brand-lavender: #abb0fd;
  }
  html, body {
    margin: 0;
    padding: 0;
    width: 1200px;
    height: 849px;
    overflow: hidden;
  }
  .folder-cover {
    position: relative;
    width: 1200px;
    height: 849px;
    background: radial-gradient(ellipse 62% 70% at 50% 50%, var(--bg-center) 0%, #2f78fd 55%, var(--bg-edge) 100%);
    font-family: "Questrial", sans-serif;
    overflow: hidden;
  }
  .bar { position: absolute; }
  .bar--corner-lavender { left: 72px; top: 0; width: 14px; height: 316px; background: var(--brand-lavender); }
  .bar--corner-yellow { left: 90px; top: 0; width: 15px; height: 215px; background: var(--brand-yellow); }
  .bar--top-left { left: 229px; top: 144px; width: 218px; height: 14px; background: var(--brand-blue); }
  .bar--top-right { left: 783px; top: 144px; width: 218px; height: 14px; background: var(--brand-blue); }

  .brand {
    position: absolute;
    left: 737px;
    top: 441px;
    width: 320px;
    text-align: center;
  }
  .brand__name {
    margin: 0;
    font-size: 46px;
    font-weight: 400;
    letter-spacing: 2px;
    line-height: 1;
    color: var(--brand-blue);
    text-transform: uppercase;
  }
  .brand__tagline {
    margin: 11px 0 0;
    font-size: 24px;
    line-height: 1;
    letter-spacing: 1.5px;
    color: var(--brand-lavender);
    white-space: nowrap;
  }

  .contact-rule { position: absolute; left: 118px; width: 246px; }
  .contact-rule--lavender { top: 570px; height: 8px; background: var(--brand-lavender); }
  .contact-rule--yellow { top: 627px; height: 8px; background: var(--brand-yellow); }
  .contact-rule--blue { top: 754px; height: 8px; background: var(--brand-blue); }

  .contact-line {
    position: absolute;
    left: 72px;
    margin: 0;
    font-size: 28px;
    line-height: 1;
    color: var(--brand-yellow);
    white-space: nowrap;
  }
  .contact-line__label { font-weight: 700; margin-right: 10px; }
  .contact-line--address { top: 588px; }
  .contact-line--phone { top: 647px; }
  .contact-line--web { top: 682px; }
  .contact-line--mail { top: 717px; }
</style>
</head>
<body>
  <main class="folder-cover">
    <div class="bar bar--corner-lavender"></div>
    <div class="bar bar--corner-yellow"></div>
    <div class="bar bar--top-left"></div>
    <div class="bar bar--top-right"></div>

    <section class="brand">
      <h1 class="brand__name">Veradine</h1>
      <p class="brand__tagline">Painting &amp; Contracting</p>
    </section>

    <div class="contact-rule contact-rule--lavender"></div>
    <p class="contact-line contact-line--address"><span class="contact-line__label">A/</span>Harbor Lane, 48</p>
    <div class="contact-rule contact-rule--yellow"></div>
    <p class="contact-line contact-line--phone"><span class="contact-line__label">T/</span>321 654 987</p>
    <p class="contact-line contact-line--web"><span class="contact-line__label">W/</span>www.veradine.net</p>
    <p class="contact-line contact-line--mail"><span class="contact-line__label">M/</span>hi@veradine.net</p>
    <div class="contact-rule contact-rule--blue"></div>
  </main>
</body>
</html>
```